Business Card Design Project

We need a buisness card for a new digital sinage company. Our target cliants are small to mediaum buisness who want to advertise on out digital sinage network

Target Market(s)

Small to medium buisness

Industry/Entity Type

Digital

Requirements
Must have
• Must have logo

```html
<!DOCTYPE html>
<html lang="en">
<head>
<meta charset="utf-8">
<title>Signo – Business Card</title>
<link rel="stylesheet" href="https://fonts.googleapis.com/css2?family=Archivo+Black&family=Arimo:wght@400;700&display=swap">
<style>
  :root {
    --page-bg: #e9e6e2;
    --card-white: #f6f6f6;
    --card-grey: #e2e2e2;
    --card-black: #050505;
    --ink: #141414;
    --brand-blue: #1e8fd0;
    --deep-blue: #1552a0;
    --brand-green: #2a9a1c;
    --brand-yellow: #f6b414;
    --white: #ffffff;
  }
  * { margin: 0; padding: 0; box-sizing: border-box; }
  html, body { width: 1200px; height: 723px; overflow: hidden; background: var(--page-bg); }
  .stage {
    width: 1200px; height: 723px;
    display: flex; align-items: center; justify-content: center; gap: 40px;
  }
  .card {
    position: relative; width: 540px; height: 310px;
    border-radius: 28px; overflow: hidden;
    box-shadow: 0 6px 18px rgba(0,0,0,.18);
  }
  .card--front { background: linear-gradient(160deg, var(--card-white) 30%, var(--card-grey) 100%); }
  .card--back { background: var(--card-black); }
  .accent-area {
    position: absolute; left: 0; right: 0; bottom: 0; height: 78px;
    background: linear-gradient(135deg, var(--brand-blue) 0%, var(--deep-blue) 100%);
  }
  .brand {
    position: absolute; display: flex; align-items: center; gap: 14px;
  }
  .brand__mark { width: 38px; height: 38px; background: var(--brand-blue); border-radius: 4px; }
  .brand__name {
    font-family: "Archivo Black", "Arial Black", sans-serif;
    font-size: 54px; line-height: 1; letter-spacing: -1px; color: var(--ink);
  }
  .card--front .brand { left: 40px; top: 136px; }
  .card--back .brand { left: 50%; top: 50%; transform: translate(-50%, -50%); }
  .card--back .brand__name { color: var(--white); font-size: 64px; }
  .contact {
    position: absolute; right: 40px; top: 34px; text-align: right;
    font-family: "Arimo", Arial, sans-serif; color: var(--ink);
  }
  .contact__name { font-size: 21px; font-weight: 700; margin-bottom: 8px; }
  .contact__line {
    display: flex; justify-content: flex-end; align-items: center; gap: 6px;
    font-size: 13px; line-height: 19px;
  }
  .contact__icon { width: 11px; height: 11px; flex: none; }
</style>
</head>
<body>
<main class="stage">
  <section class="card card--front" aria-label="Business card front">
    <div class="accent-area" role="img" aria-label="Decorative colour wave in yellow, green and blue"></div>

    <div class="brand">
      <span class="brand__mark"></span>
      <span class="brand__name">Signo</span>
    </div>

    <div class="contact">
      <p class="contact__name">Alex Morgan</p>
      <p class="contact__line">+0 987 654 321
        <svg class="contact__icon" viewBox="0 0 12 12" aria-hidden="true"><path fill="var(--deep-blue)" d="M2.5 1 L4.5 1 L5.3 3.5 L4 4.6 C4.6 6 6 7.4 7.4 8 L8.5 6.7 L11 7.5 L11 9.5 C11 10.3 10.3 11 9.5 11 C5 11 1 7 1 2.5 C1 1.7 1.7 1 2.5 1 Z"/></svg>
      </p>
      <p class="contact__line">info@signoscreens.com
        <svg class="contact__icon" viewBox="0 0 12 12" aria-hidden="true"><rect x="1" y="3" width="10" height="7" fill="none" stroke="var(--deep-blue)" stroke-width="1.4"/><path d="M1 3 L6 7 L11 3" fill="none" stroke="var(--deep-blue)" stroke-width="1.4"/></svg>
      </p>
      <p class="contact__line">www.signoscreens.com
        <svg class="contact__icon" viewBox="0 0 12 12" aria-hidden="true"><circle cx="6" cy="6" r="5" fill="var(--brand-blue)"/><path d="M1 6 H11 M6 1 C3.5 3.5 3.5 8.5 6 11 M6 1 C8.5 3.5 8.5 8.5 6 11" fill="none" stroke="var(--white)" stroke-width=".8"/></svg>
      </p>
    </div>
  </section>

  <section class="card card--back" aria-label="Business card back">
    <div class="brand">
      <span class="brand__mark"></span>
      <span class="brand__name">Signo</span>
    </div>
  </section>
</main>
</body>
</html>
```